Presentation Folder Design Project

We want a presentation folder design for a property business based in the UK. Our brand colour are Yellow and Black.

The background colour should be Yellow. Allowed colour are Yellow and Black and their shades.

INSIDE PAGE: 18.90 Width x 13.99 Height

OUTSIDE PAGE: 18.90 Width x 13.99 Height PLUS 4.02 Inches for the Reverse part to put papers. So that makes a total of 18.90 x 18.01 inches

The front side:
Should have company logo, company name "Halvorne Group" with Tag line "Talk Property - Think Halvorne"
And three UK Houses Images. See attachment.

-
The Back side:
Should have company logo, Head Quarter Images, Address, Website, email etc. See Attachment
Should have Phone number prominent and graphically presented.

-

The Inside (Left side):

Should have a "springbok" Image with the provided Text. See attachment.

The inside (right side)

Flap to carry papers preferably with a logo on the flap.

Reason: Still trying to get some balance

Reason: Just have some changes, we want Yellow as the dominant colour as that was not followed.

Reason: Still waiting for feedback from my team

Business

• The folder must have 4 pages, and use the Logo and Images we've attached.

The Background colour should be Yellow.

The Only Colour Allowed in the entire folder are Yellow, Black and Greyish Black and the shades thereof.

No other colours should be used.

ALL DESIGNERS

Please submit your designs Inner and Outer Part as ONE SINGLE design submission.

Do not Submit them separately.

```html
<!DOCTYPE html>
<html lang="en">
<head>
<meta charset="utf-8">
<title>Halvorne Group – Presentation Folder</title>
<link href="https://fonts.googleapis.com/css2?family=Hind:wght@400;500;600;700&display=swap" rel="stylesheet">
<style>
  :root{
    --yellow:#f7ea1f;
    --yellow-soft:#fbf37a;
    --yellow-deep:#e8d400;
    --black:#000;
    --greyblack:#1c1c1c;
    --white:#fff;
    --photo-frame:#fff;
  }
  *{box-sizing:border-box;margin:0;padding:0}
  html,body{width:1200px;height:1200px;overflow:hidden;background:var(--white)}
  body{position:relative;font-family:"Hind",Arial,sans-serif;color:var(--black)}
  .abs{position:absolute}

  /* Sheets */
  .sheet{position:absolute;left:167px;width:880px;height:585px;overflow:hidden}
  .sheet--outside{top:12px;background:var(--yellow)}
  .sheet--inside{top:601px;background:var(--black)}
  .fold{position:absolute;top:0;left:440px;width:1px;height:100%;background:rgba(128,128,128,.35)}

  /* Outside bands */
  .band-top{top:0;left:0;width:100%;height:35px;background:var(--black)}
  .band-top-rule{top:38px;left:0;width:100%;height:5px;background:var(--black)}
  .glow-upper{top:43px;left:0;width:100%;height:200px;
    background:radial-gradient(ellipse 60% 80% at 30% 0%,var(--yellow-soft),transparent 70%),
               radial-gradient(ellipse 60% 80% at 80% 40%,var(--yellow-soft),transparent 70%)}
  .band-photos{top:243px;left:0;width:100%;height:124px;
    background:linear-gradient(160deg,var(--black) 0%,var(--black) 40%,#2a2600 52%,var(--black) 62%,var(--black) 100%)}
  .band-photos-rule{top:367px;left:0;width:100%;height:3px;background:var(--white)}
  .band-foot-rule{top:538px;left:0;width:100%;height:6px;background:var(--black)}
  .band-foot{top:548px;left:0;width:100%;height:37px;background:var(--black)}

  .photo{position:absolute;border:3px solid var(--photo-frame)}
  .photo--hq{background:linear-gradient(180deg,#6b6b6b,#3a3a3a 55%,#9a9a9a)}
  .photo--lobby{background:linear-gradient(160deg,#bdbdbd,#4b4b4b)}
  .photo--house{background:linear-gradient(180deg,#8a8a8a 0%,#5a5a4a 45%,#2f2f26 100%)}
  .photo--animal{background:linear-gradient(180deg,#cfc9a8 0%,#8b7a55 50%,#e2dcc4 100%);border-width:2px}

  /* Back cover */
  .back-title{left:0;width:458px;top:66px;text-align:center;font-size:29px;font-weight:700;line-height:1}
  .back-contact{left:0;width:458px;top:100px;text-align:center;font-size:10px;line-height:13px;font-weight:500}
  .back-contact .label{font-weight:700;display:block}
  .back-contact p{margin-bottom:9px}
  .back-tagline{left:0;width:458px;top:370px;text-align:center;font-size:18px;font-weight:700}
  .helpline{left:124px;top:400px;width:206px;height:51px;border-radius:26px;background:var(--black);
    border:2px solid var(--greyblack);box-shadow:0 0 0 2px var(--yellow-deep) inset}
  .helpline-icon{position:absolute;left:3px;top:3px;width:45px;height:45px;border-radius:50%;background:var(--white)}
  .helpline-number{position:absolute;left:56px;top:3px;font-size:18px;font-weight:700;color:var(--white);line-height:20px}
  .helpline-label{position:absolute;left:62px;top:23px;font-size:18px;font-weight:700;color:var(--yellow);line-height:20px}
  .legal{left:0;width:458px;top:564px;text-align:center;color:var(--white);font-size:7px;font-weight:600}

  /* Brand lockup */
  .brand{display:flex;flex-direction:column;align-items:center;position:absolute}
  .brand-row{display:flex;align-items:center;gap:6px}
  .brand-mark{background:var(--black)}
  .brand-name{font-weight:700;color:var(--black);line-height:1}
  .brand-tag{color:var(--black);font-weight:400}
  .brand--small{left:0;width:458px;top:510px}
  .brand--small .brand-mark{width:12px;height:12px}
  .brand--small .brand-name{font-size:14px}
  .brand--small .brand-tag{font-size:8px;margin-top:2px}
  .brand--front{left:440px;width:496px;top:486px}
  .brand--front .brand-mark{width:18px;height:18px}
  .brand--front .brand-name{font-size:20px}
  .brand--front .brand-tag{font-size:11px;margin-top:4px}

  /* Front cover */
  .front-title{left:440px;width:442px;top:96px;text-align:center;font-size:45px;font-weight:700;line-height:1}
  .front-tagline{left:471px;top:157px;width:377px;height:46px;border-radius:12px;background:var(--black);
    color:var(--white);font-size:24px;line-height:48px;text-align:center;font-weight:500}

  /* Inside */
  .inside-glow{inset:0;background:radial-gradient(ellipse 50% 20% at 75% 32%,rgba(60,60,60,.35),transparent 70%)}
  .emblem-title{right:676px;top:278px;font-size:26px;font-weight:700;color:var(--yellow);line-height:1}
  .emblem-latin{right:676px;top:304px;font-size:10px;color:var(--yellow)}
  .emblem-note{right:676px;top:320px;font-size:6px;font-style:italic;font-weight:600;color:var(--yellow)}
  .divider{left:218px;top:161px;width:2px;height:209px;background:var(--yellow-deep)}
  .story{left:228px;top:168px;width:192px;color:var(--yellow);font-size:7px;font-weight:700;line-height:12px}
  .story ul{list-style:none;margin-top:12px}
  .story li{position:relative;padding-left:9px;margin-bottom:4px;font-size:6px}
  .story li::before{content:"";position:absolute;left:0;top:3px;width:5px;height:5px;border-radius:50%;background:var(--yellow)}
  .inside-foot{left:0;top:535px;width:440px;height:50px;background:var(--yellow)}
  .inside-foot-rule{left:0;top:541px;height:8px;width:440px;background:var(--black)}
  .flap{left:440px;top:386px;width:440px;height:199px}
  .brand--flap{left:440px;width:440px;top:502px}
  .brand--flap .brand-mark{width:13px;height:13px}
  .brand--flap .brand-name{font-size:15px}
  .brand--flap .brand-tag{font-size:8px;margin-top:3px}
</style>
</head>
<body>

<section class="sheet sheet--outside">
  <div class="abs band-top"></div>
  <div class="abs band-top-rule"></div>
  <div class="abs glow-upper"></div>
  <div class="abs band-photos"></div>
  <div class="abs band-photos-rule"></div>
  <div class="abs band-foot-rule"></div>
  <div class="abs band-foot"></div>

  <h2 class="abs back-title">Halvorne Group</h2>
  <div class="abs back-contact">
    <p><span class="label">Head Office</span>Unit C4, Marlow House Business Centre<br>Riverside Enterprise Park, Dock Road,<br>Leeds, LS9 4QT</p>
    <p><span class="label">Website</span>www.halvornegroup.co.uk</p>
    <p><span class="label">Email</span>admin@halvornegroup.co.uk</p>
  </div>
  <div class="photo photo--hq" style="left:97px;top:258px;width:120px;height:93px" role="img" aria-label="Head office building exterior"></div>
  <div class="photo photo--lobby" style="left:240px;top:258px;width:121px;height:93px" role="img" aria-label="Head office reception interior"></div>

  <div class="abs back-tagline">Talk Property - Think Halvorne</div>
  <div class="abs helpline">
    <div class="helpline-icon">
      <svg width="45" height="45" viewBox="0 0 45 45" aria-hidden="true">
        <path d="M14 11c2-1 4 0 5 2l2 5c1 2 0 3-1 4l-2 1c1 3 4 6 7 8l1-2c1-1 3-2 4-1l5 2c2 1 3 3 2 5l-1 2c-1 2-4 3-7 2-8-3-14-9-17-17-1-3 0-6 2-7z" fill="#000"/>
      </svg>
    </div>
    <div class="helpline-number">0845 000 4127</div>
    <div class="helpline-label">24/7 Helpline</div>
  </div>

  <div class="brand brand--small">
    <div class="brand-row"><span class="brand-mark"></span><span class="brand-name">Halvorne Group</span></div>
    <span class="brand-tag">Talk Property - Think Halvorne</span>
  </div>
  <div class="abs legal">Company Registration No. 0000000 VAT No. 000 123 4567 Data Protection No. Z0000000</div>

  <h1 class="abs front-title">Halvorne Group</h1>
  <div class="abs front-tagline">Talk Property - Think Halvorne</div>
  <div class="photo photo--house" style="left:471px;top:265px;width:116px;height:80px" role="img" aria-label="Red-brick detached UK cottage"></div>
  <div class="photo photo--house" style="left:600px;top:265px;width:116px;height:80px" role="img" aria-label="Victorian terraced UK houses"></div>
  <div class="photo photo--house" style="left:729px;top:265px;width:116px;height:80px" role="img" aria-label="Stone UK village house"></div>

  <div class="brand brand--front">
    <div class="brand-row"><span class="brand-mark"></span><span class="brand-name">Halvorne Group</span></div>
    <span class="brand-tag">Talk Property - Think Halvorne</span>
  </div>

  <div class="fold"></div>
</section>

<section class="sheet sheet--inside">
  <div class="abs inside-glow"></div>

  <div class="photo photo--animal" style="left:73px;top:167px;width:131px;height:102px" role="img" aria-label="Gazelle standing in open grassland"></div>
  <h2 class="abs emblem-title">The Halvorne</h2>
  <div class="abs emblem-latin">(Gazella halvornis)</div>
  <div class="abs emblem-note">Our emblem: swift, sure-footed and always ahead of the herd.</div>

  <div class="abs divider"></div>
  <div class="abs story">
    <p>The halvorne is a medium-sized, brown and white gazelle, native to southern Africa. We chose the halvorne as our emblem because:</p>
    <ul>
      <li>They're quick, like us. We match sellers to buyers in days or weeks - or on a date of your choice!</li>
      <li>They can leap to great heights, like we do to ensure our tailor-made solutions fit your needs!</li>
      <li>They can long-jump, like we do to carry you over traditional hassles, thanks to our clear, simple processes.</li>
      <li>They look after each other like we look after our clients, with honesty and reliability guided by our charter and code of ethics.</li>
      <li>Their population is growing, like our company. We're expanding thanks to our expertise, integrity and exemplary service that no one can match!</li>
    </ul>
  </div>

  <div class="abs inside-foot"></div>
  <div class="abs inside-foot-rule"></div>

  <svg class="abs flap" viewBox="0 0 440 199" preserveAspectRatio="none" aria-hidden="true">
    <polygon points="15,0 440,0 440,199 0,199 0,158" fill="#f7ea1f"/>
  </svg>
  <div class="brand brand--flap">
    <div class="brand-row"><span class="brand-mark"></span><span class="brand-name">Halvorne Group</span></div>
    <span class="brand-tag">Talk Property - Think Halvorne</span>
  </div>

  <div class="fold"></div>
</section>

</body>
</html>
```